STICKER DESIGN required for packaging. UK START UP TEA BUSINESS

We are looking for a design for a sticker that will be applied to packaging for our teas! We are a new start up Tea business based in the UK called 'BrookLeafs'
Selling quality loose leaf tea and teabags via our online shop and also face to face at farmers markets / food shows and eventually in our own tea emporium. We will be marketing our teas to hotels, cafes, delis etc. too
We carry every day teas eg. breakfast blends and also speciality and rare teas to offer customers the chance to try something new. Tea as a treat / ritual / indulgence / healthy lifestyle choice / modern
The design will initially be printed on vinyl stickers and then applied to the tea packaging (pouch bags in matte black and matte silver), in the future the design may be printed direct onto our packaging. The sticker design will need to be scalable as the size of the pouch bag varies dependant on the tea.
The sticker we have in mind is a leaf shape (sketch attached)
colour green to match our logo
It will include our logo (files attached)
Text to be included on the sticker is
- www.brookleafs.co.uk
- Welbury, England
- The tea type eg. Green
It will need to complement both black and silver pouches that we are using to package our teas (see attached image of our pouches)
Colours - green leaf, see our corporate colours (green & orange) on our logo files attached. We also like silver and black.
Font - nothing to swirly, must be easy to read on the packaging
once a sticker design is agreed for the initial tea type (Green) we will require additional files for each tea type that we stock. Just the tea type (Green) to be updated - the rest of the design to stay the same. The tea types we stock are listed below
Green
Black
Oolong
White
Herbal
Blended
Happy to answer any questions and aim to give feedback daily! Thank you for your interest

```html
<!DOCTYPE html>
<html lang="en">
<head>
<meta charset="utf-8">
<title>BrookLeafs – Tea Type Leaf Stickers</title>
<link rel="stylesheet" href="https://fonts.googleapis.com/css2?family=Nunito:wght@400;600;700&display=swap">
<style>
  :root {
    --leaf-green: #086937;
    --brand-orange: #e3981f;
    --type-green: #8cc63f;
    --stage-light: #ffffff;
    --stage-dark: #9c9c9c;
  }
  html, body {
    margin: 0;
    padding: 0;
    width: 1200px;
    height: 1000px;
    overflow: hidden;
  }
  .sheet {
    position: relative;
    width: 1200px;
    height: 1000px;
    background: radial-gradient(ellipse 62% 62% at 50% 50%, var(--stage-light) 72%, var(--stage-dark) 130%);
    font-family: "Nunito", sans-serif;
  }
  .sticker {
    position: absolute;
    width: 260px;
    height: 260px;
    overflow: visible;
  }
  .sticker--r1 { top: 180px; }
  .sticker--r2 { top: 567px; }
  .sticker--c1 { left: 78px; }
  .sticker--c2 { left: 470px; }
  .sticker--c3 { left: 862px; }
  .leaf-shape { fill: var(--leaf-green); }
  .leaf-web,
  .leaf-place {
    fill: var(--brand-orange);
    font-size: 8.5px;
    letter-spacing: 0.9px;
    font-weight: 600;
  }
  .leaf-brand {
    fill: var(--brand-orange);
    font-size: 20px;
    font-weight: 700;
  }
  .leaf-type {
    fill: var(--type-green);
    font-size: 6px;
    letter-spacing: 2.6px;
    font-weight: 600;
  }
</style>
</head>
<body>
<main class="sheet">
  <svg width="0" height="0" style="position:absolute" aria-hidden="true">
    <defs>
      <path id="leaf-outline" d="M252,3 C200,20 150,25 110,45 C40,80 5,140 3,215 C2,235 6,248 12,253 C16,256 20,252 18,246 C14,230 14,210 30,198 C60,180 120,180 170,160 C220,140 236,90 252,3 Z"/>
    </defs>
  </svg>

  <svg class="sticker sticker--r1 sticker--c1" viewBox="0 0 260 260" role="img" aria-label="BrookLeafs Green tea sticker">
    <use href="#leaf-outline" class="leaf-shape"/>
    <text class="leaf-web" x="142" y="38" transform="rotate(-14 142 38)">www.brookleafs.co.uk</text>
    <text class="leaf-brand" x="117" y="120" text-anchor="middle">BrookLeafs</text>
    <text class="leaf-type" x="118" y="139" text-anchor="middle">GREEN</text>
    <text class="leaf-place" x="30" y="193" transform="rotate(-11 30 193)">Welbury, England</text>
  </svg>

  <svg class="sticker sticker--r1 sticker--c2" viewBox="0 0 260 260" role="img" aria-label="BrookLeafs Black tea sticker">
    <use href="#leaf-outline" class="leaf-shape"/>
    <text class="leaf-web" x="142" y="38" transform="rotate(-14 142 38)">www.brookleafs.co.uk</text>
    <text class="leaf-brand" x="117" y="120" text-anchor="middle">BrookLeafs</text>
    <text class="leaf-type" x="118" y="139" text-anchor="middle">BLACK</text>
    <text class="leaf-place" x="30" y="193" transform="rotate(-11 30 193)">Welbury, England</text>
  </svg>

  <svg class="sticker sticker--r1 sticker--c3" viewBox="0 0 260 260" role="img" aria-label="BrookLeafs Oolong tea sticker">
    <use href="#leaf-outline" class="leaf-shape"/>
    <text class="leaf-web" x="142" y="38" transform="rotate(-14 142 38)">www.brookleafs.co.uk</text>
    <text class="leaf-brand" x="117" y="120" text-anchor="middle">BrookLeafs</text>
    <text class="leaf-type" x="118" y="139" text-anchor="middle">OOLONG</text>
    <text class="leaf-place" x="30" y="193" transform="rotate(-11 30 193)">Welbury, England</text>
  </svg>

  <svg class="sticker sticker--r2 sticker--c1" viewBox="0 0 260 260" role="img" aria-label="BrookLeafs Blended tea sticker">
    <use href="#leaf-outline" class="leaf-shape"/>
    <text class="leaf-web" x="142" y="38" transform="rotate(-14 142 38)">www.brookleafs.co.uk</text>
    <text class="leaf-brand" x="117" y="120" text-anchor="middle">BrookLeafs</text>
    <text class="leaf-type" x="118" y="139" text-anchor="middle">BLENDED</text>
    <text class="leaf-place" x="30" y="193" transform="rotate(-11 30 193)">Welbury, England</text>
  </svg>

  <svg class="sticker sticker--r2 sticker--c2" viewBox="0 0 260 260" role="img" aria-label="BrookLeafs Herbal tea sticker">
    <use href="#leaf-outline" class="leaf-shape"/>
    <text class="leaf-web" x="142" y="38" transform="rotate(-14 142 38)">www.brookleafs.co.uk</text>
    <text class="leaf-brand" x="117" y="120" text-anchor="middle">BrookLeafs</text>
    <text class="leaf-type" x="118" y="139" text-anchor="middle">HERBAL</text>
    <text class="leaf-place" x="30" y="193" transform="rotate(-11 30 193)">Welbury, England</text>
  </svg>

  <svg class="sticker sticker--r2 sticker--c3" viewBox="0 0 260 260" role="img" aria-label="BrookLeafs White tea sticker">
    <use href="#leaf-outline" class="leaf-shape"/>
    <text class="leaf-web" x="142" y="38" transform="rotate(-14 142 38)">www.brookleafs.co.uk</text>
    <text class="leaf-brand" x="117" y="120" text-anchor="middle">BrookLeafs</text>
    <text class="leaf-type" x="118" y="139" text-anchor="middle">WHITE</text>
    <text class="leaf-place" x="30" y="193" transform="rotate(-11 30 193)">Welbury, England</text>
  </svg>
</main>
</body>
</html>
```